Car Detailing product label for 750ML Clear Bottle

I need a label for various product with differente color for each products but in the same size bottle each time. It's only for our purpose no commercial application. I need a template with differente color but same design. The name for product it's : Tidal Quartz. We dont have any logo because it's only for us. We like like car silhouette in the logo or in background or something like that.

And for the product we have many like : APC Cleaner, Drying Aid, Wheel Cleaner and some other.

```html
<!DOCTYPE html>
<html lang="en">
<head>
<meta charset="utf-8">
<title>Tidal Quartz – APC Cleaner Label</title>
<link rel="stylesheet" href="https://fonts.googleapis.com/css2?family=Oswald:wght@400;600&family=Roboto:wght@500;700&display=swap">
<style>
  :root {
    --page: #ffffff;
    --ink-black: #0b0b0b;
    --header-top: #2b2b2b;
    --header-bottom: #121212;
    --silver: #dfe2e6;
    --silver-dark: #9ea3aa;
    --blue-light: #3b7ddb;
    --blue-top: #2463c6;
    --blue-bottom: #1a3b8f;
    --bar-text: #2a2a2a;
    --white: #ffffff;
  }
  * { margin: 0; padding: 0; box-sizing: border-box; }
  html, body {
    width: 1016px;
    height: 1200px;
    overflow: hidden;
    background: var(--page);
  }
  .label {
    position: absolute;
    left: 160px;
    top: 124px;
    width: 707px;
    height: 942px;
    overflow: hidden;
    background: var(--ink-black);
  }
  .label-art {
    position: absolute;
    inset: 0;
    width: 100%;
    height: 100%;
    display: block;
  }
  .brand-name {
    position: absolute;
    left: 0;
    top: 60px;
    width: 658px;
    text-align: center;
    font-family: "Oswald", sans-serif;
    font-weight: 600;
    font-size: 46px;
    line-height: 46px;
    letter-spacing: 3px;
    color: var(--silver);
    text-transform: uppercase;
  }
  .product-name {
    position: absolute;
    left: 320px;
    top: 642px;
    font-family: "Oswald", sans-serif;
    font-weight: 400;
    font-size: 92px;
    line-height: 80px;
    letter-spacing: 1px;
    color: var(--silver);
    text-transform: uppercase;
  }
  .quality-bar {
    position: absolute;
    left: 320px;
    top: 812px;
    width: 346px;
    height: 40px;
    background: linear-gradient(90deg, var(--silver), #f4f5f7 50%, var(--silver));
    display: flex;
    align-items: center;
    justify-content: center;
    font-family: "Roboto", sans-serif;
    font-weight: 500;
    font-size: 21px;
    letter-spacing: 3px;
    color: var(--bar-text);
  }
  .volume {
    position: absolute;
    right: 41px;
    top: 878px;
    font-family: "Roboto", sans-serif;
    font-weight: 700;
    font-size: 36px;
    line-height: 40px;
    color: var(--white);
  }
</style>
</head>
<body>
  <main class="label">
    <svg class="label-art" viewBox="0 0 589 785" preserveAspectRatio="none" aria-hidden="false">
      <defs>
        <linearGradient id="header-fill" x1="0" y1="0" x2="0" y2="1">
          <stop offset="0" stop-color="var(--header-top)"/>
          <stop offset="1" stop-color="var(--header-bottom)"/>
        </linearGradient>
        <linearGradient id="texture-fill" x1="0" y1="0" x2="1" y2="1">
          <stop offset="0" stop-color="#1e1e1e"/>
          <stop offset="1" stop-color="#070707"/>
        </linearGradient>
        <linearGradient id="swoosh-fill" x1="0" y1="0" x2="1" y2="0">
          <stop offset="0" stop-color="var(--silver-dark)"/>
          <stop offset="0.5" stop-color="#f2f3f5"/>
          <stop offset="1" stop-color="var(--silver-dark)"/>
        </linearGradient>
        <linearGradient id="blue-fill" x1="0" y1="0" x2="0" y2="1">
          <stop offset="0" stop-color="var(--blue-top)"/>
          <stop offset="1" stop-color="var(--blue-bottom)"/>
        </linearGradient>
        <radialGradient id="car-sketch-fill" cx="0.45" cy="0.6" r="0.6">
          <stop offset="0" stop-color="#8a8d92" stop-opacity="0.55"/>
          <stop offset="1" stop-color="#1a1a1a" stop-opacity="0"/>
        </radialGradient>
      </defs>

      <rect class="texture-area" x="0" y="120" width="589" height="665" fill="url(#texture-fill)" role="img" aria-label="Dark carbon-fibre texture background"/>
      <rect class="header-band" x="0" y="0" width="589" height="140" fill="url(#header-fill)"/>
      <path class="header-swoosh" d="M0,122 C150,150 400,162 589,116 L589,126 C400,174 150,162 0,132 Z" fill="url(#swoosh-fill)"/>

      <rect class="car-sketch" x="17" y="217" width="410" height="255" fill="url(#car-sketch-fill)" role="img" aria-label="White line sketch of a sports car seen from the rear three-quarter view"/>

      <path class="accent-stripe" d="M70,785 C200,560 380,330 589,212 L589,222 C385,342 212,570 84,785 Z" fill="var(--blue-light)"/>
      <path class="blue-panel" d="M95,785 C230,580 400,362 589,234 L589,785 Z" fill="url(#blue-fill)"/>
    </svg>

    <h1 class="brand-name">Tidal<br>Quartz</h1>
    <h2 class="product-name">APC<br>Cleaner</h2>
    <div class="quality-bar">TOP QUALITY</div>
    <div class="volume">750ml</div>
  </main>
</body>
</html>
```